依頼詳細
開店にはすこしまに合わないのですが、OPENチラシの作成をお願いいたします。

チラシ全体の雰囲気から癒しの雰囲気を感じ目にとまるデザインをお願いしたいです。

ある程度の構成は手書きで見にくくて申し訳ないのですが、添付しておりますので、
参考にして作って戴きたいです。

決してメニューの料金が安くないので、少し高級感も感じ、でも高級感がありすぎてチラシを見た方がハードルが高く感じていまわないようにしたいです。

記載項目
店名/住所/電話番号/QRコード/メニュー表/地図
サイズ
A4
ページ数
両面
希望イメージ
シンプル 複雑
単色 カラフル
暗い 明るい
日常 高級
遊び心 厳粛
未来的 伝統的
女性的 男性的
希望する色
青系
納品ファイル
• 高解像度JPG (.jpg)
• イラストレーター形式 (.ai)
補足説明
QRコードですが、まだ予約サイトが公開されておらず、10月28日公開予定で、URLをおくれるのが、28日以降になってしまいますので、その部分だけ余白であけておいて頂いて作成お願いします。28日以降に追加予約URLを添付いたします。
■ 選んだ理由

シンプルで見やすく全体的にバランスよくスッキリとまとまった印象を受け、
お客様がパッと見てもわかりやすいし目にとまるような気がしましたので、選ばせて戴きました。

■ 提案者全員のお礼・コメント

皆様この度は素敵なデザインのご提案戴き誠にありがとうございました。

また機会がございましたら、その際はよろしくお願いいたします。

```html
<!DOCTYPE html>
<html lang="ja">
<head>
<meta charset="utf-8">
<title>sora グランドオープン</title>
<link href="https://fonts.googleapis.com/css2?family=Noto+Serif+JP:wght@400;600&family=Noto+Sans+JP:wght@400;500&family=Cormorant+Garamond:wght@500;600&display=swap" rel="stylesheet">
<style>
  :root{
    --navy:#1f3564;
    --blue:#2b4a86;
    --white:#ffffff;
    --paper:#fbfbfc;
    --badge:#7fa6d6;
    --photo-light:#e9e4df;
    --photo-mid:#c9b8a8;
    --photo-skin:#d9b9a0;
  }
  *{margin:0;padding:0;box-sizing:border-box;}
  html,body{width:849px;height:1200px;overflow:hidden;background:var(--paper);}
  .flyer{position:relative;width:849px;height:1200px;background:var(--paper);font-family:"Noto Serif JP",serif;color:var(--navy);overflow:hidden;}
  .navy-band{position:absolute;left:0;top:560px;width:849px;height:640px;background:var(--navy);}
  .brand{position:absolute;top:38px;left:0;width:100%;text-align:center;}
  .brand-tag{font-family:"Noto Sans JP",sans-serif;font-size:15px;letter-spacing:2px;color:var(--navy);}
  .brand-name{font-family:"Cormorant Garamond",serif;font-weight:600;font-size:50px;line-height:1;color:var(--navy);margin-top:2px;}
  .brand-kana{display:flex;align-items:center;justify-content:center;gap:8px;font-family:"Noto Sans JP",sans-serif;font-size:10px;color:var(--navy);margin-top:4px;}
  .brand-kana::before,.brand-kana::after{content:"";width:40px;height:1px;background:var(--navy);}
  .date{position:absolute;top:158px;width:100%;text-align:center;font-family:"Noto Sans JP",sans-serif;font-weight:400;font-size:66px;color:var(--blue);letter-spacing:1px;line-height:1;}
  .headline{position:absolute;top:238px;width:100%;text-align:center;font-family:"Noto Sans JP",sans-serif;font-weight:400;font-size:70px;color:var(--blue);letter-spacing:1px;line-height:1;}
  .photo-main{position:absolute;left:128px;top:330px;width:721px;height:420px;background:linear-gradient(110deg,var(--photo-light) 0%,var(--photo-skin) 45%,var(--photo-mid) 100%);}
  .photo-inset{position:absolute;left:128px;width:145px;background:linear-gradient(160deg,var(--photo-skin),#8c6a55);border:3px solid var(--white);}
  .photo-inset.one{top:340px;height:180px;}
  .photo-inset.two{top:528px;height:195px;}
  .lead{position:absolute;top:820px;width:100%;text-align:center;color:var(--white);}
  .lead-title{font-size:34px;font-weight:600;letter-spacing:4px;}
  .lead-sub{font-size:21px;margin-top:10px;letter-spacing:1px;}
  .body{position:absolute;top:955px;left:135px;width:560px;font-family:"Noto Sans JP",sans-serif;font-size:13.5px;line-height:1.72;color:var(--white);}
  .badge{position:absolute;left:748px;top:1083px;width:92px;height:92px;border-radius:50%;background:var(--badge);color:var(--white);font-family:"Noto Sans JP",sans-serif;font-size:12px;line-height:1.4;display:flex;align-items:center;justify-content:center;text-align:center;}
</style>
</head>
<body>
<main class="flyer">
  <div class="navy-band"></div>

  <header class="brand">
    <p class="brand-tag">頭ほぐし専門店</p>
    <p class="brand-name">sora</p>
    <p class="brand-kana">ソラ</p>
  </header>

  <p class="date">2021.11.1</p>
  <h1 class="headline">GRAND OPEN!!</h1>

  <div class="photo-main" role="img" aria-label="施術者がお客様の頭をほぐしている写真"></div>
  <div class="photo-inset one" role="img" aria-label="両手で頭をほぐす手元の写真"></div>
  <div class="photo-inset two" role="img" aria-label="頭頂部を指で押すヘッドスパの写真"></div>

  <section class="lead">
    <h2 class="lead-title">〜 極上の癒しを 〜</h2>
    <p class="lead-sub">あなたの疲れの正体は実は脳疲労だった!?</p>
  </section>

  <p class="body">
    現代の忙しい日々をお過ごしの皆様。<br>
    お仕事・家事・育児・教育・人間関係などでさまざまなストレスを抱えていらっしゃる方も多いと思います。そのストレスにより、脳疲労がたまっています。<br>
    脳疲労によって自律神経が乱れ、血流が悪くなり、体のあちこちに不調をもたらします。<br>
    頭痛・目の疲れ・肩こり・首こり・睡眠不足(スマホやパソコンの見過ぎ)<br>
    その脳疲労を解消し、全身の調子を整える事を目的とした水を使用しない<br>
    ドライヘッドスパ専門店です。<br>
    ぜひ、心身のお疲れを癒しにお越しくださいませ。
  </p>

  <div class="badge">メニュー<br>クーポン<br>詳細</div>
</main>
</body>
</html>
```